LVM IT Solutions Provider

Please read attached documentation completely before beginning Project. Thank you!

Mark Forge Project Requirements

Thank you for your interest in this design contest. We are always welcome to questions and are looking forward to seeing what you can come up with.

The logo is located on the current site homepage http://www.lumavex.com/

Bootstrap

We work on a Bootstrap platform with our custom built CMS. We require all designs to be

sized accordingly with the bootstrap grid system found here: http://getframelyn.com/css/#grid

Start of Competition Requirements

At the start of a competition, we are looking for general Home Page Design concepts and interior page design concepts as well.

HOME PAGE DESIGN

Any changes requested by the client in the original designs

Responsive Tablet View (using standard bootstrap media queries, we need to see an

example of a tablet size home page view)

Responsive Phone View (using standard bootstrap media queries, we need to see an

example of a phone size home page view)

INTERIOR PAGE DESIGN

These pages are general content pages. Our CMS allows for the creation of unlimited

pages and gives the client control of adding them. Interior Page Designs can be built

with 1 column, 2 columns (either right side bar or left sidebar)

Examples of buttons and button states,

Examples of drop down menus

Examples of H1 through H5 plus body copy

We uploaded a clean logo to use on the project. Thank you.

We added a updated Creative Brief document to help out. Please take a look thanks!

```html
<!DOCTYPE html>
<html lang="en">
<head>
<meta charset="utf-8">
<title>LVM – Technology Solutions</title>
<link rel="stylesheet" href="https://fonts.googleapis.com/css2?family=Roboto+Condensed:wght@400;700&family=Arimo:wght@400;700&display=swap">
<style>
:root{
  --brand:#1d4f91;
  --brand-light:#4a90d9;
  --ink:#222;
  --muted:#555;
  --line:#e4e4e4;
  --band:#2c3039;
  --band-tile:#353943;
  --footer:#dcdcdc;
  --bottom:#171717;
  --social:#a9a9a9;
  --white:#fff;
}
*{margin:0;padding:0;box-sizing:border-box}
html,body{width:764px;height:1200px;overflow:hidden;background:var(--white)}
body{position:relative;font-family:"Arimo",Arial,sans-serif;color:var(--ink)}
.abs{position:absolute}
a{text-decoration:none}

/* header */
.brand{left:110px;top:12px;display:flex;align-items:center;gap:8px}
.brand-dot{width:16px;height:16px;border-radius:50%;background:var(--brand)}
.brand-name{font-family:"Roboto Condensed",sans-serif;font-weight:700;font-size:38px;line-height:44px;color:var(--brand);letter-spacing:1px}
.brand-sub{left:110px;top:56px;font-family:"Roboto Condensed",sans-serif;font-weight:700;font-size:7.5px;color:var(--brand);letter-spacing:.3px}
.contact-bar{right:108px;top:9px;display:flex;gap:14px;font-size:7px;line-height:9px;color:var(--muted)}
.contact-item{display:flex;align-items:center;gap:4px;white-space:nowrap}
.social-top{left:541px;top:27px;display:flex;gap:2px}
.social-top span{width:18px;height:18px;background:var(--social)}
.social-top span.red{background:#c9302c}
.social-top span.search{background:var(--white);border:1px solid var(--brand-light);display:flex;align-items:center;justify-content:center}
.nav{right:110px;top:55px;display:flex;gap:14px;font-family:"Roboto Condensed",sans-serif;font-weight:700;font-size:8px;color:#333}
.nav .active{color:var(--brand)}

/* hero */
.hero{left:0;top:80px;width:764px;height:318px;background:linear-gradient(180deg,#8f8a80 0%,#c8c2b4 35%,#9da56e 62%,#8a8a85 75%,#6f6f6c 100%)}
.hero-title{left:0;top:262px;width:764px;text-align:center;font-family:"Roboto Condensed",sans-serif;font-weight:700;font-size:22px;line-height:26px;color:var(--white);text-shadow:0 1px 3px rgba(0,0,0,.5)}
.btn{display:flex;align-items:center;justify-content:center;font-family:"Roboto Condensed",sans-serif;font-weight:700;font-size:7.5px;letter-spacing:.3px}
.btn-primary{left:272px;top:334px;width:107px;height:20px;background:var(--brand);color:var(--white)}
.btn-ghost{left:385px;top:334px;width:107px;height:20px;border:1px solid var(--white);color:var(--white)}

/* welcome */
.section-title{left:0;width:764px;text-align:center;font-family:"Roboto Condensed",sans-serif;font-weight:400;font-size:18px;color:#222}
.welcome-text{left:190px;top:466px;width:384px;text-align:center;font-size:7px;line-height:9.5px;color:#333}
.badges{left:297px;top:500px;display:flex;gap:12px;align-items:center}
.badge{background:#cfd6e4}
.btn-outline{left:329px;top:550px;width:107px;height:20px;border:1px solid #555;color:#333;font-weight:400}
.divider{left:123px;top:595px;width:518px;height:1px;background:var(--line)}

/* hiring */
.tile{width:112px;height:90px;border:1px solid #f2f2f2;display:flex;flex-direction:column;align-items:center;justify-content:center;gap:12px;font-family:"Roboto Condensed",sans-serif;font-size:11px;color:#222}
.tile svg{width:32px;height:32px}
.tile.active{background:#f5f5f5;color:var(--brand);font-weight:700;border-color:#f5f5f5}

/* social band */
.band{left:0;top:970px;width:764px;height:54px;background:var(--band)}
.band-tile{top:981px;width:32px;height:32px;background:var(--band-tile)}
.band-tile.active{background:var(--brand-light)}

/* footer */
.footer{left:0;top:1024px;width:764px;height:141px;background:var(--footer)}
.f-head{top:1045px;font-family:"Roboto Condensed",sans-serif;font-weight:400;font-size:12px;color:#222}
.f-text{font-size:6.5px;line-height:8px;color:#444}
.f-links{left:250px;top:1064px;list-style:none;font-size:6.5px;line-height:12.5px;color:#444}
.f-links li::before{content:"›";margin-right:3px}
.f-links .active{color:var(--brand-light)}
.post{left:384px;display:flex;gap:4px}
.post-thumb{width:31px;height:31px;background:linear-gradient(135deg,#b9bfc7,#6d7480)}
.bottom{left:0;top:1165px;width:764px;height:35px;background:var(--bottom)}
.copyright{left:110px;top:1179px;font-size:6.5px;color:#666}
.btn-footer{left:548px;top:1172px;width:107px;height:20px;border:1px solid var(--white);color:var(--white)}
</style>
</head>
<body>

<header>
  <div class="abs brand"><span class="brand-name">LVM</span><span class="brand-dot"></span></div>
  <div class="abs brand-sub">LUMAVEX RESEARCH CORPORATION</div>
  <div class="abs contact-bar">
    <span class="contact-item"><svg width="9" height="7" viewBox="0 0 9 7"><rect x=".5" y=".5" width="8" height="6" fill="none" stroke="#1d4f91"/><path d="M.5 .5 4.5 4 8.5 .5" fill="none" stroke="#1d4f91"/></svg>info@lumavex.com</span>
    <span class="contact-item"><svg width="8" height="8" viewBox="0 0 8 8"><path d="M1 1c1-1 2 1 2 2s-1 1 0 2 1 0 2 0 3 1 2 2C5 9-1 3 1 1z" fill="#1d4f91"/></svg>P: (555) 014-2270</span>
  </div>
  <div class="abs social-top"><span></span><span class="red"></span><span></span><span></span><span class="search"><svg width="11" height="11" viewBox="0 0 11 11"><circle cx="4.5" cy="4.5" r="3.3" fill="none" stroke="#1d4f91" stroke-width="1.3"/><path d="M7 7l3.3 3.3" stroke="#1d4f91" stroke-width="1.6"/></svg></span></div>
  <nav class="abs nav"><span class="active">HOME</span><span>ABOUT LVM</span><span>DIVISIONS</span><span>PRODUCTS/SERVICES</span></nav>
</header>

<section>
  <div class="abs hero" role="img" aria-label="Business people in suits assembling large black gears in an open field with a city skyline behind"></div>
  <h1 class="abs hero-title">TECHNOLOGY SOLUTIONS FOR NATIONAL<br>DEFENSE &amp; GLOBAL SECURITY</h1>
  <a class="abs btn btn-primary">CONTACT US</a>
  <a class="abs btn btn-ghost">LEARN MORE</a>
</section>

<section>
  <h2 class="abs section-title" style="top:434px">WELCOME</h2>
  <p class="abs welcome-text">Since 1988, Lumavex Research Corporation has been providing innovative and cost-effective products and services to customers worldwide. We are a vital source for leading-edge technology solutions that help our customers respond to opportunities faster, achieve more from their operations, and exceed their requirements.</p>
  <div class="abs badges">
    <div class="badge" style="width:32px;height:28px;border-radius:50%"></div>
    <div class="badge" style="width:28px;height:32px;background:#27344f"></div>
    <div class="badge" style="width:84px;height:30px;background:#e8eef5"></div>
  </div>
  <a class="abs btn btn-outline">LEARN MORE</a>
  <div class="abs divider"></div>
</section>

<section>
  <h2 class="abs section-title" style="top:623px">WE'RE HIRING</h2>

  <div class="abs tile" style="left:124px;top:659px"><svg viewBox="0 0 32 32"><circle cx="12" cy="10" r="5"/><circle cx="21" cy="10" r="5"/><path d="M3 26c0-6 4-9 9-9s9 3 9 9zM14 26c1-5 3-8 7-8 5 0 8 3 8 8z"/></svg>A Career at LVM</div>
  <div class="abs tile" style="left:259px;top:659px"><svg viewBox="0 0 32 32"><circle cx="16" cy="16" r="13"/><circle cx="16" cy="16" r="9" fill="#fff"/><path d="M11 16l4 4 7-8" fill="none" stroke="#000" stroke-width="3"/></svg>Benefits</div>
  <div class="abs tile active" style="left:394px;top:659px"><svg viewBox="0 0 32 32"><rect x="11" y="1" width="10" height="5" fill="#1d4f91"/><path d="M12 7h8l3 18-7 6-7-6z" fill="#4a90d9"/></svg>Corporate Culture</div>
  <div class="abs tile" style="left:529px;top:659px"><svg viewBox="0 0 32 32" fill="none" stroke="#000" stroke-width="3" stroke-linejoin="round"><path d="M11 11l5-8 5 8"/><path d="M18 8l3 3 3-1"/><path d="M24 16l5 9H20"/><path d="M23 22l-3 3 3 3"/><path d="M12 25H3l4-8"/><path d="M4 19l3-2 2 3"/></svg>Our Hiring Process</div>

  <div class="abs tile" style="left:124px;top:764px"><svg viewBox="0 0 32 32"><circle cx="16" cy="10" r="7"/><path d="M4 30c0-8 5-12 12-12s12 4 12 12z"/></svg>Student Opportunities</div>
  <div class="abs tile" style="left:259px;top:764px"><svg viewBox="0 0 32 32"><circle cx="12" cy="12" r="8" fill="none" stroke="#000" stroke-width="3"/><path d="M18 18l10 10" stroke="#000" stroke-width="4"/><circle cx="24" cy="9" r="4"/></svg>Job Search</div>
  <div class="abs tile" style="left:394px;top:764px"><svg viewBox="0 0 32 32"><circle cx="16" cy="16" r="14" fill="none" stroke="#000" stroke-width="2.5"/><circle cx="16" cy="9" r="2"/><rect x="14" y="13" width="4" height="11"/></svg>How to Apply</div>
  <div class="abs tile" style="left:529px;top:764px"><svg viewBox="0 0 32 32"><rect x="15" y="4" width="2" height="24"/><rect x="5" y="7" width="22" height="2"/><path d="M2 17h10a5 4 0 0 1-10 0zM20 17h10a5 4 0 0 1-10 0zM10 28h12v2H10z"/><path d="M7 9l-5 8M7 9l5 8M25 9l-5 8M25 9l5 8" stroke="#000" stroke-width="1"/></svg>EEO is the Law</div>

  <div class="abs tile" style="left:259px;top:870px"><svg viewBox="0 0 32 32"><circle cx="16" cy="16" r="14" fill="none" stroke="#000" stroke-width="2"/><path d="M16 16V2a14 14 0 0 1 14 14z"/><path d="M16 16l12 7M16 16L6 27" stroke="#000" stroke-width="1.5"/></svg>Diversity</div>
  <div class="abs tile" style="left:394px;top:870px"><svg viewBox="0 0 32 32"><rect x="2" y="5" width="22" height="22" fill="none" stroke="#000" stroke-width="2.5"/><rect x="2" y="5" width="22" height="5"/><circle cx="22" cy="22" r="5" fill="#fff" stroke="#000" stroke-width="2.5"/><path d="M25 25l5 5" stroke="#000" stroke-width="3"/></svg>Recruiting Events</div>
</section>

<section>
  <div class="abs band"></div>
  <div class="abs band-tile" style="left:176px"></div>
  <div class="abs band-tile" style="left:223px"></div>
  <div class="abs band-tile" style="left:270px"></div>
  <div class="abs band-tile" style="left:317px"></div>
  <div class="abs band-tile active" style="left:365px"></div>
  <div class="abs band-tile" style="left:412px"></div>
  <div class="abs band-tile" style="left:459px"></div>
  <div class="abs band-tile" style="left:506px"></div>
  <div class="abs band-tile" style="left:554px"></div>
</section>

<footer>
  <div class="abs footer"></div>
  <h3 class="abs f-head" style="left:110px">About Us</h3>
  <p class="abs f-text" style="left:110px;top:1066px;width:130px">Pellentesque habitant morbi tristique senectus et netus et malesuada fames ac turpis egestas. Vestibulum tortor quam, feugiat vitae, ultricies eget, tempor sit amet, ante.</p>
  <p class="abs f-text" style="left:110px;top:1112px;width:130px">Pellentesque habitant morbi tristique senectus.</p>

  <h3 class="abs f-head" style="left:250px">Company</h3>
  <ul class="abs f-links"><li class="active">HOME</li><li>ABOUT LVM</li><li>DIVISIONS</li><li>PRODUCTS/SERVICES</li></ul>

  <h3 class="abs f-head" style="left:384px">Latest Blog</h3>
  <div class="abs post" style="top:1064px"><div class="post-thumb" role="img" aria-label="Blog thumbnail of business people"></div><div class="f-text" style="width:90px">Pellentesque habitant morbi tristique senectus<br><br>Posted 17 Aug 2013</div></div>
  <div class="abs post" style="top:1102px"><div class="post-thumb" role="img" aria-label="Blog thumbnail of a team meeting"></div><div class="f-text" style="width:90px">Pellentesque habitant morbi tristique senectus<br><br>Posted 17 Aug 2013</div></div>

  <h3 class="abs f-head" style="left:529px">Address</h3>
  <p class="abs f-text" style="left:529px;top:1066px;width:120px"><b>Lumavex Research Corporation</b><br>1400 Harbor Crest Drive,<br>Suite 210 North<br>Riverton, GA 30100<br>P: (555) 014-2270</p>

  <div class="abs bottom"></div>
  <p class="abs copyright">Copyright 2014 © Lumavex Research Corporation. All rights reserved.</p>
  <a class="abs btn btn-footer">CONTACT US</a>
</footer>

</body>
</html>
```